bright lane coaching needs snazzy business card that serves a dual purpose

business card needed for a Bright Lane Coaching company that takes people out on the road to teach them proficiency on their bike.
My business logo is attached. I have grey and aqua colours with my logo.
i really like bitumen/tarmac/ road in the design somehow but that is up to you.
I think navy blue will go well with my colours too. see how you go.

I want this card to look REALLY good.
the back of the card may be used for emergency contact details too
In case of Emergency I am:
Name:

Emergency Contact name
emergency contact Phone number:

• details that are essential are:
• logo
• Name: Marnie HOLT
• ABN: 53 916 204 871
• phone number: 0438 152 964
• facebook logo
• * ride tuition & proficiency
• * skills practice
• * maintenance 101
• * bike fitting service
• * cater for all ages & abilities
• backpage:
• logo
• skills confidence enjoyment
• some space for writing
• nothing girly. The business will already naturally attract women, it needs to appeal to both genders

```html
<!DOCTYPE html>
<html lang="en">
<head>
<meta charset="utf-8">
<title>Bright Lane Coaching – Business Card</title>
<link rel="stylesheet" href="https://fonts.googleapis.com/css2?family=Open+Sans:wght@400;600;700&display=swap">
<style>
  :root {
    --aqua: #72d6ca;
    --aqua-deep: #4fbfb2;
    --aqua-ink: #2f9f93;
    --charcoal: #3a3b3d;
    --paper: #ffffff;
    --stage: #e9e6e1;
  }
  * { box-sizing: border-box; margin: 0; padding: 0; }
  html, body { width: 1200px; height: 1023px; overflow: hidden; }
  body {
    background: var(--stage);
    font-family: "Open Sans", Arial, sans-serif;
    position: relative;
  }
  .card {
    position: absolute;
    width: 560px;
    height: 320px;
    border-radius: 26px;
    overflow: hidden;
    box-shadow: 0 10px 28px rgba(0,0,0,.18);
  }
  .card-front { left: 70px; top: 130px; background: var(--paper); }
  .card-back { left: 570px; top: 570px; background: var(--aqua); }
  .card-art { position: absolute; inset: 0; }

  /* wordmark */
  .wordmark {
    position: absolute;
    display: flex;
    align-items: center;
    gap: 12px;
    color: var(--charcoal);
    font-weight: 600;
  }
  .wordmark-dot {
    width: 18px; height: 18px; border-radius: 50%;
    background: var(--charcoal);
    flex: none;
  }
  .wordmark-name { line-height: 1.05; letter-spacing: 1px; text-transform: uppercase; }
  .card-front .wordmark { left: 34px; top: 124px; }
  .card-front .wordmark-name { font-size: 30px; }
  .card-back .wordmark { left: 150px; top: 36px; color: var(--paper); }
  .card-back .wordmark-dot { background: var(--paper); width: 22px; height: 22px; }
  .card-back .wordmark-name { font-size: 34px; }

  /* front details */
  .details {
    position: absolute;
    right: 28px; top: 26px;
    text-align: right;
    color: var(--charcoal);
    font-size: 11px;
    line-height: 1.6;
  }
  .person-name { font-size: 19px; font-weight: 700; line-height: 1.1; }
  .person-role { font-size: 10px; margin-bottom: 8px; }
  .contact-line { display: flex; justify-content: flex-end; align-items: center; gap: 6px; }
  .contact-icon {
    width: 12px; height: 12px; border-radius: 2px;
    background: var(--charcoal);
    display: inline-flex; align-items: center; justify-content: center;
  }
  .services { list-style: none; margin-top: 8px; }
  .services li::after { content: " •"; }
  .abn { margin-top: 8px; font-weight: 600; }

  /* back */
  .writing-band {
    position: absolute;
    left: 0; right: 0; top: 128px; height: 112px;
    background: var(--paper);
    border-bottom: 5px solid var(--charcoal);
    padding: 20px 28px 0;
  }
  .writing-line {
    height: 26px;
    border-bottom: 1.5px dashed #b9c2c1;
  }
  .emergency {
    position: absolute;
    left: 28px; bottom: 20px;
    color: var(--charcoal);
    font-size: 13px;
    line-height: 1.55;
  }
  .emergency strong { font-weight: 700; }
</style>
</head>
<body>

<section class="card card-front" aria-label="Card front">
  <svg class="card-art" viewBox="0 0 560 320" width="560" height="320" aria-hidden="true">
    <path d="M320 0 C 280 110, 380 200, 348 320 L560 320 L560 0 Z" fill="var(--charcoal)"/>
    <path d="M330 0 C 292 110, 392 200, 360 320 L560 320 L560 0 Z" fill="var(--aqua)"/>
  </svg>

  <div class="wordmark">
    <span class="wordmark-dot"></span>
    <span class="wordmark-name">Bright Lane<br>Coaching</span>
  </div>

  <div class="details">
    <p class="person-name">Marnie HOLT</p>
    <p class="person-role">Director</p>
    <p class="contact-line">0438 152 964
      <span class="contact-icon">
        <svg width="8" height="8" viewBox="0 0 24 24"><path fill="#fff" d="M6.6 10.8a15.1 15.1 0 0 0 6.6 6.6l2.2-2.2c.3-.3.7-.4 1-.2 1.1.4 2.3.6 3.6.6.6 0 1 .4 1 1V20c0 .6-.4 1-1 1A17 17 0 0 1 3 4c0-.6.4-1 1-1h3.5c.6 0 1 .4 1 1 0 1.3.2 2.5.6 3.6.1.3 0 .7-.2 1z"/></svg>
      </span>
    </p>
    <p class="contact-line">/marnieHOLT <span class="contact-icon"></span></p>
    <ul class="services">
      <li>Ride Tuition &amp; Proficiency</li>
      <li>Skills Practice</li>
      <li>Maintenance 101</li>
      <li>Bike Fitting Service</li>
      <li>Cater For All Ages &amp; Abilities</li>
    </ul>
    <p class="abn">ABN: 53 916 204 871</p>
  </div>
</section>

<section class="card card-back" aria-label="Card back">
  <div class="wordmark">
    <span class="wordmark-dot"></span>
    <span class="wordmark-name">Bright Lane<br>Coaching</span>
  </div>

  <div class="writing-band">
    <div class="writing-line"></div>
    <div class="writing-line"></div>
    <div class="writing-line"></div>
  </div>

  <div class="emergency">
    <p>In case of Emergency I am <strong>Marnie HOLT</strong></p>
    <p>Emergency Contact name emergency contact <strong>0438 152 964</strong></p>
  </div>
</section>

</body>
</html>
```